Brisk Parcel
Brisk Parcel - Transportation
Creative Brief
Modern
Faisal K. Marzouq
CEO
Salwiya Block 4 St 9 House 2
marzouq.faisal@lunaquill.com
www.qirmazkitchenry.com
Logo of the company and quote "Swift Paths Carry"
velmdraw47 velmdraw47
Please upload your logo.

```html
<!DOCTYPE html>
<html lang="en">
<head>
<meta charset="utf-8">
<title>Brisk Parcel – Stationery</title>
<link rel="stylesheet" href="https://fonts.googleapis.com/css2?family=Didact+Gothic&family=Nunito+Sans:ital,wght@0,400;0,700;0,800;1,800&display=swap">
<style>
  :root {
    --blue: #1f4f9c;
    --blue-deep: #1a4390;
    --orange: #e9a51a;
    --paper: #ffffff;
    --ink: #1d1d1d;
    --rule: #9a9a9a;
    --backdrop: #e6e7ea;
    --body: "Didact Gothic", "Century Gothic", sans-serif;
    --strong: "Nunito Sans", "Arial", sans-serif;
  }
  * { box-sizing: border-box; margin: 0; padding: 0; }
  html, body { width: 1200px; height: 1012px; overflow: hidden; }
  body { background: var(--backdrop); font-family: var(--body); color: var(--ink); position: relative; }

  .brand { display: flex; align-items: center; gap: 8px; }
  .brand-mark { width: 22px; height: 22px; background: var(--orange); }
  .brand-name { font-family: var(--strong); font-weight: 800; color: var(--blue); font-size: 26px; letter-spacing: .5px; text-transform: uppercase; }

  /* Invoice sheet */
  .invoice { position: absolute; left: 40px; top: 40px; width: 560px; height: 792px; background: var(--paper); box-shadow: 0 2px 10px rgba(0,0,0,.12); padding: 40px; }
  .invoice .brand { position: absolute; left: 40px; top: 46px; }
  .invoice-head { position: absolute; right: 40px; top: 40px; text-align: left; }
  .invoice-title { font-family: var(--strong); font-weight: 800; font-style: italic; color: var(--blue); font-size: 34px; letter-spacing: 1px; }
  .invoice-reg { font-size: 10px; line-height: 1.3; }
  .invoice-meta { position: absolute; right: 92px; top: 150px; font-size: 12px; line-height: 1.9; }
  .bill-to { position: absolute; left: 40px; top: 140px; width: 230px; border: 1px solid var(--rule); }
  .bill-to-head { background: var(--blue); color: #fff; font-size: 12px; padding: 4px 10px; }
  .bill-to-body { font-size: 10px; line-height: 1.3; padding: 8px 12px 12px; }
  .bill-to-body .who { font-size: 11px; margin-bottom: 6px; }

  table { border-collapse: collapse; width: 480px; position: absolute; left: 40px; font-size: 11px; }
  th { font-weight: 400; color: #fff; text-align: center; padding: 4px 6px; }
  td { border: 1px solid var(--rule); height: 22px; }
  .ref-table { top: 300px; }
  .ref-table th { background: var(--orange); }
  .ref-table th:first-child { text-align: left; }
  .line-table { top: 372px; }
  .line-table th { background: var(--blue); }
  .line-table .body-row td { height: 300px; }
  .line-table .subtotal-row td { height: 24px; }
  .line-table .blank { border: none; }
  .line-table .subtotal-label { font-size: 10px; padding-left: 6px; }

  /* Business cards */
  .card { position: absolute; width: 420px; height: 240px; background: var(--paper); border-radius: 12px; overflow: hidden; box-shadow: 0 2px 10px rgba(0,0,0,.14); }
  .card-front { left: 740px - 0px; left: 640px; top: 40px; }
  .card-front .brand { position: absolute; left: 60px; top: 70px; }
  .card-front .brand-name { font-size: 34px; }
  .card-front .brand-mark { width: 30px; height: 30px; }
  .card-front .site { position: absolute; left: 0; bottom: 34px; width: 180px; font-size: 11px; color: var(--blue); padding-left: 16px; border-bottom: 2px solid var(--blue); padding-bottom: 4px; }
  .tagline-band { position: absolute; left: 180px; right: 0; bottom: 26px; height: 30px; background: var(--orange); color: var(--blue); font-family: var(--strong); font-weight: 800; font-style: italic; font-size: 18px; display: flex; align-items: center; padding-left: 18px; }

  .card-back { left: 640px; top: 310px; }
  .card-back .person { position: absolute; left: 24px; top: 22px; }
  .person-name { color: var(--blue); font-size: 22px; letter-spacing: .5px; }
  .person-role { color: var(--orange); font-size: 12px; }
  .card-back .brand { position: absolute; right: 22px; top: 68px; }
  .card-back .brand-name { font-size: 22px; }

  .wave { position: absolute; left: 0; bottom: 0; width: 100%; }
  .contact { position: absolute; color: #fff; font-size: 10px; line-height: 1.35; }
  .contact .address { margin-bottom: 6px; }
  .contact li { list-style: none; display: flex; align-items: center; gap: 5px; }
  .contact svg { width: 9px; height: 9px; fill: var(--orange); flex: none; }
  .card-back .contact { left: 22px; bottom: 22px; }

  /* Envelope */
  .envelope { position: absolute; left: 640px; top: 580px; width: 520px; height: 260px; background: var(--paper); overflow: hidden; box-shadow: 0 2px 10px rgba(0,0,0,.12); }
  .envelope .contact { left: 30px; bottom: 26px; font-size: 12px; }
  .envelope .contact svg { width: 11px; height: 11px; }
</style>
</head>
<body>

<section class="invoice" aria-label="Invoice">
  <div class="brand"><span class="brand-mark"></span><span class="brand-name">Brisk Parcel</span></div>
  <div class="invoice-head">
    <h1 class="invoice-title">INVOICE</h1>
    <p class="invoice-reg">Company Registration No: 000000<br>VAT No: xxx-xx-xxxxxxx</p>
  </div>
  <div class="invoice-meta"><p>Date</p><p>Invoice No</p></div>

  <div class="bill-to">
    <div class="bill-to-head">To</div>
    <div class="bill-to-body">
      <p class="who">Lena Corwell</p>
      <p>Company Limited<br>PO Box 456789<br>County<br>12345<br>Country</p>
    </div>
  </div>

  <table class="ref-table">
    <colgroup><col style="width:80px"><col style="width:240px"><col style="width:80px"><col style="width:80px"></colgroup>
    <tr><th>PO No.</th><th>REFERENCE</th><th>TERMS</th><th>DUE DATE</th></tr>
    <tr><td></td><td></td><td></td><td></td></tr>
  </table>

  <table class="line-table">
    <colgroup><col style="width:60px"><col style="width:240px"><col style="width:60px"><col style="width:60px"><col style="width:60px"></colgroup>
    <tr><th></th><th>Description</th><th>QTY</th><th>Price</th><th>Amount</th></tr>
    <tr class="body-row"><td></td><td></td><td></td><td></td><td></td></tr>
    <tr class="subtotal-row"><td class="blank"></td><td class="blank"></td><td class="blank"></td><td class="subtotal-label">SUBTOTAL</td><td></td></tr>
  </table>
</section>

<section class="card card-front" aria-label="Business card front">
  <div class="brand"><span class="brand-mark"></span><span class="brand-name">Brisk Parcel</span></div>
  <p class="site">www.qirmazkitchenry.com</p>
  <p class="tagline-band">Swift Paths Carry</p>
</section>

<section class="card card-back" aria-label="Business card back">
  <div class="person">
    <p class="person-name">Faisal K. Marzouq</p>
    <p class="person-role">CEO</p>
  </div>
  <div class="brand"><span class="brand-mark"></span><span class="brand-name">Brisk Parcel</span></div>
  <svg class="wave" viewBox="0 0 420 150" height="150" preserveAspectRatio="none" aria-hidden="true">
    <path d="M0 40 C70 0 140 10 210 70 C280 125 360 130 420 95 L420 150 L0 150 Z" fill="var(--orange)"/>
    <path d="M0 52 C70 12 140 22 210 82 C280 136 360 140 420 104 L420 150 L0 150 Z" fill="#fff"/>
    <path d="M0 58 C70 18 140 28 210 88 C280 140 360 145 420 112 L420 150 L0 150 Z" fill="var(--blue)"/>
  </svg>
  <div class="contact">
    <p class="address">Salwiya Block 4 St 9 House 2</p>
    <ul>
      <li><svg viewBox="0 0 10 10"><path d="M1 3h8v2H7V4H3v1H1zM2 5h6l1 4H1z"/></svg>50123456</li>
      <li><svg viewBox="0 0 10 10"><rect x="2.5" y="0.5" width="5" height="9" rx="1"/></svg>50987654</li>
      <li><svg viewBox="0 0 10 10"><path d="M0 2h10v6H0z M0 2l5 3 5-3" /></svg>marzouq.faisal@lunaquill.com</li>
      <li><svg viewBox="0 0 10 10"><circle cx="5" cy="5" r="4.5"/></svg>www.qirmazkitchenry.com</li>
    </ul>
  </div>
</section>

<section class="envelope" aria-label="Envelope">
  <svg class="wave" viewBox="0 0 520 190" height="190" preserveAspectRatio="none" aria-hidden="true">
    <path d="M0 50 C90 0 190 10 270 80 C360 160 450 170 520 130 L520 190 L0 190 Z" fill="var(--orange)"/>
    <path d="M0 64 C90 14 190 24 270 94 C360 172 450 182 520 142 L520 190 L0 190 Z" fill="#fff"/>
    <path d="M0 72 C90 22 190 32 270 102 C360 178 450 188 520 150 L520 190 L0 190 Z" fill="var(--blue)"/>
  </svg>
  <div class="contact">
    <p class="address">Salwiya Block 4 St 9 House 2</p>
    <ul>
      <li><svg viewBox="0 0 10 10"><path d="M1 3h8v2H7V4H3v1H1zM2 5h6l1 4H1z"/></svg>50123456</li>
      <li><svg viewBox="0 0 10 10"><rect x="2.5" y="0.5" width="5" height="9" rx="1"/></svg>50987654</li>
      <li><svg viewBox="0 0 10 10"><path d="M0 2h10v6H0z M0 2l5 3 5-3" /></svg>marzouq.faisal@lunaquill.com</li>
      <li><svg viewBox="0 0 10 10"><circle cx="5" cy="5" r="4.5"/></svg>www.qirmazkitchenry.com</li>
    </ul>
  </div>
</section>

</body>
</html>
```